Construction Directory Website Flyer

We need a postcard size +/- or somewhere around that size (something standard) flyer designed for our construction directory website. Leave a spot for tagline. Call to action is 'register your company now'. I am thinking many mini pictures of different construction to show that it is for the entire construction industry. Logo and screenshot of the homepage of the website is attached. Use same theme as webpage.

Target Market(s)

Construction Industry

Industry/Entity Type

Construction

Font styles to use
Sans Serif

Requirements
Must have
• Call to action
• Colors to match logo
• Area to add description and details.
Nice to have
• Construction Images
Should not have
• No Cartoonish types of things

```html
<!DOCTYPE html>
<html lang="en">
<head>
<meta charset="utf-8">
<title>Buildlink Hub Flyer</title>
<link rel="stylesheet" href="https://fonts.googleapis.com/css2?family=Questrial&family=Mulish:wght@400;500&family=Montserrat:wght@600&family=Lobster&display=swap">
<style>
  :root {
    --red: #e8391c;
    --red-dark: #c92c12;
    --slate: #4f5963;
    --slate-deep: #3f4851;
    --ink: #1f1f1f;
    --paper: #ffffff;
    --backdrop: #e8e5e0;
  }
  * { box-sizing: border-box; margin: 0; padding: 0; }
  html, body { width: 1200px; height: 1000px; overflow: hidden; background: var(--backdrop); }
  .canvas { position: relative; width: 1200px; height: 1000px; }
  .flyer {
    position: absolute; left: 267px; top: 72px; width: 666px; height: 855px;
    background: var(--paper); box-shadow: 0 6px 22px rgba(0,0,0,.25); overflow: hidden;
  }
  .hero {
    position: absolute; left: 0; top: 0; width: 666px; height: 354px;
    background: linear-gradient(165deg, #d9dadb 0%, #e2b27a 22%, #e8913f 38%, #d98a45 48%, #e9ecef 62%, #cfdcea 80%, #b9cbdd 100%);
  }
  .brand-panel { position: absolute; left: 0; top: 0; width: 378px; height: 100px; }
  .brand {
    position: absolute; left: 18px; top: 27px; display: flex; align-items: center; gap: 14px;
  }
  .brand-mark { width: 46px; height: 46px; background: var(--red); }
  .brand-name {
    font-family: "Montserrat", sans-serif; font-weight: 600; font-size: 28px; color: var(--slate);
  }
  .slate-strip { position: absolute; left: 300px; top: 354px; width: 366px; height: 14px; background: var(--slate); }
  .headline-box { position: absolute; left: 0; top: 311px; width: 345px; height: 102px; }
  .headline {
    position: absolute; left: 20px; top: 322px;
    font-family: "Questrial", sans-serif; font-weight: 400; font-size: 23px; line-height: 27px;
    color: var(--paper); letter-spacing: .2px;
  }
  .description {
    position: absolute; left: 19px; top: 424px; width: 287px;
    font-family: "Mulish", sans-serif; font-size: 14px; line-height: 16.1px;
    color: var(--ink); text-align: justify; hyphens: auto;
  }
  .gallery-tile {
    position: absolute; border: 4px solid var(--paper); box-shadow: 0 1px 5px rgba(0,0,0,.35);
  }
  .tile-frame   { left: 314px; top: 385px; width: 164px; height: 86px; background: linear-gradient(180deg, #dfe3e6 0%, #a88d63 45%, #6f7072 100%); }
  .tile-tools   { left: 489px; top: 385px; width: 161px; height: 86px; background: linear-gradient(160deg, #9c9996 0%, #6e6a66 100%); }
  .tile-tower   { left: 314px; top: 512px; width: 164px; height: 110px; background: linear-gradient(180deg, #2f6a93 0%, #6a8fa6 35%, #7d5550 65%, #5a4645 100%); }
  .tile-crew    { left: 489px; top: 512px; width: 161px; height: 110px; background: linear-gradient(180deg, #4e6a44 0%, #848178 55%, #9a958c 100%); }
  .tile-digger  { left: 314px; top: 637px; width: 164px; height: 111px; background: linear-gradient(180deg, #7d8387 0%, #c9b89e 55%, #8a7763 100%); }
  .tile-cranes  { left: 489px; top: 637px; width: 161px; height: 111px; background: linear-gradient(180deg, #5a98cf 0%, #9cc4e6 55%, #58606a 100%); }
  .cta {
    position: absolute; left: 0; width: 666px; top: 752px; text-align: center;
    font-family: "Lobster", cursive; font-size: 30px; color: var(--red);
  }
  .contact-bar {
    position: absolute; left: 0; top: 800px; width: 666px; height: 55px;
    background: linear-gradient(180deg, var(--slate) 0%, var(--slate-deep) 100%);
    font-family: "Mulish", sans-serif; font-size: 12.5px; color: var(--paper);
  }
  .contact-item { position: absolute; top: 16px; display: flex; align-items: center; gap: 9px; }
  .contact-phone { left: 19px; }
  .contact-email { left: 169px; }
  .contact-web   { left: 416px; }
  .contact-icon { width: 23px; height: 23px; }
</style>
</head>
<body>
<div class="canvas">
  <article class="flyer">
    <div class="hero" role="img" aria-label="Smiling construction manager in a white hard hat in front of a team of workers and orange excavators"></div>

    <svg class="brand-panel" viewBox="0 0 378 100" aria-hidden="true">
      <polygon points="0,0 378,0 338,100 0,100" fill="#ffffff"/>
    </svg>
    <div class="brand">
      <span class="brand-mark"></span>
      <span class="brand-name">Buildlink Hub</span>
    </div>

    <div class="slate-strip"></div>
    <svg class="headline-box" viewBox="0 0 345 102" aria-hidden="true">
      <polygon points="0,0 345,0 290,102 0,102" fill="#e8391c"/>
      <polygon points="0,95 294,95 290,102 0,102" fill="#c92c12"/>
    </svg>
    <h1 class="headline">BUILT BY<br>CONSTRUCTION&nbsp; FOR<br>CONSTRUCTION</h1>

    <p class="description">Lorem ipsum dolor sit amet, consectetur adipiscing elit. Quisque id felis sed orci placerat feugiat. Donec tellus elit, rhoncus at mauris non, rutrum convallis augue. Aliquam fringilla ultricies viverra. Proin dictum neque vitae massa fringilla tincidunt. In tincidunt mi quis nulla ultricies tempor. Nam imperdiet bibendum leo in ultricies. In tincidunt nulla eget pellentesque tempus.<br>In hac habitasse platea dictumst. Proin a enim sed nisi euismod tristique. Donec malesuada eleifend nunc eu dictum. Morbi faucibus mi ex, sit amet elementum elit pretium eu. Maecenas hendrerit lacus nunc, non tristique libero vestibulum ut. Donec in dapibus ipsum. Quisque eleifend risus ex, et tempor dui varius ut. Vestibulum vestibulum lectus eget mi venenatis, eu laoreet odio tristique.</p>

    <div class="gallery-tile tile-frame" role="img" aria-label="House under construction with timber roof frame"></div>
    <div class="gallery-tile tile-tools" role="img" aria-label="Hand plane and wood shavings on a workbench"></div>
    <div class="gallery-tile tile-tower" role="img" aria-label="High-rise building under construction with tower crane"></div>
    <div class="gallery-tile tile-crew" role="img" aria-label="Workers in safety vests laying out a site"></div>
    <div class="gallery-tile tile-digger" role="img" aria-label="Red excavator on a construction site"></div>
    <div class="gallery-tile tile-cranes" role="img" aria-label="Concrete tower rising with cranes against blue sky"></div>

    <p class="cta">register your company now</p>

    <footer class="contact-bar">
      <div class="contact-item contact-phone">
        <svg class="contact-icon" viewBox="0 0 24 24" aria-hidden="true">
          <circle cx="12" cy="12" r="12" fill="#fff"/>
          <path d="M8.6 6.5l1.8 2.6-1.1 1.4c.7 1.6 1.9 2.9 3.6 3.7l1.3-1.1 2.6 1.8-1 2c-4.3-.3-8.1-4.1-8.3-8.4z" fill="#4f5963"/>
        </svg>
        <span>000-555-0142</span>
      </div>
      <div class="contact-item contact-email">
        <svg class="contact-icon" viewBox="0 0 24 24" aria-hidden="true">
          <circle cx="12" cy="12" r="12" fill="#fff"/>
          <rect x="6.5" y="8" width="11" height="8" fill="#4f5963"/>
          <path d="M6.5 8l5.5 4.5L17.5 8" stroke="#fff" stroke-width="1.2" fill="none"/>
        </svg>
        <span>info@buildlinkhub.com</span>
      </div>
      <div class="contact-item contact-web">
        <svg class="contact-icon" viewBox="0 0 24 24" aria-hidden="true">
          <circle cx="12" cy="12" r="12" fill="#fff"/>
          <g stroke="#4f5963" stroke-width="1.3" fill="none">
            <circle cx="12" cy="12" r="6"/>
            <ellipse cx="12" cy="12" rx="2.6" ry="6"/>
            <path d="M6 12h12M7 9h10M7 15h10"/>
          </g>
        </svg>
        <span>www.buildlinkhub.com</span>
      </div>
    </footer>
  </article>
</div>
</body>
</html>
```